Scrum Master & Agile IT Coach Needing Business Website

Hello, my name is Brent Holloway
I am a project manger, scrum master, & agile coach. I work with IT development teams on major projects for Fortune 500 companies . My project management business has a website and can be found here: www.tq-keystride.example

I have launched a new company, ALL focused on IT Agile Coaching, I am looking to have a website created for my new company - the name of the new company is: Pins and Dials - Agile IT Coaching and Training.
I have a logo and it is provided in the materials. I like to logo; I am open to different color pallets.

The website will have a total of 7 pages; I have content for 5 of the 7 pages prepared; the other 2 pages will say under construction.

Page 1 Who am I, What I do, My Experience
Demonstrated experience and progression from Scrum Master to
Program Manager to Coach

Page 2 Pins & Dials - Agile Team Coaching
teams working major IT projects, multiple months/years

Page 3 Coaching @ the Team Level

Page 4 Coaching @ the Program Level ; LYNQ BQR level

Pages 5 -6 Under Construction

Page 7 Presentations, Slide Decks, Reference Materials

Mentor Nook need to have this highlighted somewhere Monthly Blog
Updates

Industry/Entity Type

IT development

Coding

Coded - Design and coding required

Number of Pages Required

5+ page

Requirements
Must have
• the website must be bold - I want those who visit to remember coming to my coaching site
Nice to have
• nice to have will be a modern / futuristic website; I work with IT developers, I want a website they will like
Should not have
• should not be stiff - it should be professional but fun

```html
<!DOCTYPE html>
<html lang="en">
<head>
<meta charset="utf-8">
<title>Pins &amp; Dials – Agile IT Coaching &amp; Training</title>
<link href="https://fonts.googleapis.com/css2?family=Barlow:wght@400;500;600;700&display=swap" rel="stylesheet">
<style>
:root{
  --ink:#111418;
  --text:#2b2f36;
  --brand:#1a64b8;
  --brand-deep:#1766b8;
  --card:#0b8fd8;
  --navy:#1c2f63;
  --orange:#f3a73a;
  --sky:#2a9be0;
  --pale:#eef4fa;
  --footer:#3b3b3b;
  --white:#ffffff;
}
*{box-sizing:border-box;margin:0;padding:0}
html,body{width:1200px;height:2642px;overflow:hidden}
body{font-family:'Barlow',sans-serif;color:var(--text);background:var(--white);position:relative}
.abs{position:absolute}
a{color:inherit;text-decoration:none}

.site-header{position:absolute;left:0;top:0;width:1200px;height:105px;background:var(--pale)}
.brand-box{position:absolute;left:0;top:0;width:282px;height:104px;background:var(--white);clip-path:polygon(0 0,100% 0,100% 58%,242px 100%,0 100%)}
.brand-name{position:absolute;left:48px;top:32px;display:flex;align-items:center;gap:10px}
.brand-dot{width:30px;height:30px;border-radius:4px;background:var(--navy)}
.brand-text{font-weight:600;font-size:17px;line-height:1.05;color:var(--navy)}
.brand-text small{display:block;font-size:9px;letter-spacing:.5px;font-weight:600}
.topbar{position:absolute;left:372px;top:20px;width:690px;height:30px;border-bottom:1px solid #c9ced6;font-size:12px;color:var(--ink)}
.topbar .contact{position:absolute;top:2px;display:flex;align-items:center;gap:6px}
.socials{position:absolute;right:2px;top:0;display:flex;gap:16px}
.socials span{width:20px;height:20px;border-radius:50%;background:#555}
.main-nav{position:absolute;left:372px;top:73px;display:flex;gap:16px;font-size:12px;font-weight:500;color:var(--ink)}

.hero{position:absolute;left:0;top:105px;width:1200px;height:545px;background:linear-gradient(180deg,var(--pale) 0%,#fafcfe 100%)}
.hero-deco{position:absolute;right:0;top:10px;width:600px;height:530px;background:radial-gradient(ellipse at 70% 50%,#d6e8f6 0%,rgba(214,232,246,0) 70%)}
.hero-photo{position:absolute;left:620px;top:30px;width:440px;height:505px;background:linear-gradient(160deg,#eef1f4 0%,#b9b1a5 55%,#e5e7ea 100%)}
.hero-name{position:absolute;left:144px;top:84px;font-size:33px;font-weight:600;color:var(--ink)}
.hero-role{position:absolute;left:142px;top:124px;font-size:20px;color:var(--ink)}
.hero-bio{position:absolute;left:144px;top:170px;width:445px;font-size:12.5px;line-height:19.2px;color:var(--ink)}
.btn{display:flex;align-items:center;justify-content:center;font-size:14px;font-weight:500}
.btn-solid{background:var(--brand);color:var(--white)}
.hero .btn{position:absolute;left:144px;top:366px;width:167px;height:48px}

.designations{position:absolute;left:0;top:650px;width:1200px;height:385px}
.section-title{position:absolute;font-size:27px;font-weight:600;color:var(--ink);text-transform:uppercase;white-space:nowrap}
.badge{position:absolute;top:92px;width:150px;height:150px;border-radius:50%}
.profile-btn{position:absolute;top:277px;height:49px}

.what-we-do{position:absolute;left:0;top:1035px;width:1200px;height:700px;background:linear-gradient(180deg,#eef5fb 0%,#ffffff 70%)}
.service{position:absolute;width:190px;height:190px;border-radius:50%;background:var(--white);box-shadow:0 14px 28px rgba(30,60,100,.15);display:flex;flex-direction:column;align-items:center;justify-content:center;text-align:center;font-size:13px;font-weight:600;color:var(--ink);line-height:19px;text-transform:uppercase}
.service svg{margin-bottom:14px}

.exp-band{position:absolute;left:0;top:1910px;width:1200px;height:495px;background:var(--brand-deep)}
.exp-card{position:absolute;top:1818px;width:340px;height:397px;background:var(--card);color:var(--white);clip-path:polygon(0 0,100% 0,100% 78%,262px 100%,0 100%);padding:34px 34px 0}
.exp-card h3{font-size:17px;font-weight:500;text-transform:uppercase;line-height:24px;min-height:48px}
.exp-card ul{list-style:none;margin-top:20px;font-size:12.5px;line-height:15px}
.exp-card li{display:flex;gap:12px;margin-bottom:11px}
.exp-card li.gap{margin-bottom:22px}
.exp-card li svg{flex:none;margin-top:1px}
.cta-title{position:absolute;left:0;width:1240px;top:2258px;text-align:center;font-size:27px;font-weight:600;color:var(--white)}
.btn-light{position:absolute;left:525px;top:2317px;width:167px;height:48px;background:var(--white);color:var(--brand)}

.site-footer{position:absolute;left:0;top:2405px;width:1200px;height:237px;background:var(--footer);color:var(--white)}
.footer-title{position:absolute;font-size:17px;font-weight:500;text-transform:uppercase}
.footer-links{position:absolute;left:624px;top:76px;list-style:none;font-size:12.5px;line-height:19.2px;text-transform:uppercase}
</style>
</head>
<body>

<header class="site-header">
  <div class="brand-box">
    <div class="brand-name"><span class="brand-dot"></span><div class="brand-text">PINS &amp; DIALS<small>AGILE IT COACHING &amp; TRAINING L.L.C</small></div></div>
  </div>
  <div class="topbar">
    <div class="contact" style="left:0">
      <svg width="18" height="14" viewBox="0 0 18 14"><rect x="1" y="1" width="16" height="12" fill="none" stroke="#222" stroke-width="1.4"/><path d="M1 1l8 6 8-6" fill="none" stroke="#222" stroke-width="1.4"/></svg>
      mail@company.com</div>
    <div class="contact" style="left:180px">
      <svg width="16" height="16" viewBox="0 0 16 16"><path d="M3 1l3 3-2 2c1 2 3 4 5 5l2-2 3 3-2 3C7 14 2 9 1 3z" fill="none" stroke="#222" stroke-width="1.3"/></svg>
      0000 000 000</div>
    <div class="socials" aria-label="Social links"><span></span><span></span><span></span><span></span></div>
  </div>
  <nav class="main-nav">
    <a>Home</a><a>Agile team coaching</a><a>Coaching @ the Team Level</a><a>Coaching @ the Program Level ; LYNQ BQR level</a>
  </nav>
</header>

<section class="hero">
  <div class="hero-deco" role="img" aria-label="Soft hexagon network pattern"></div>
  <div class="hero-photo" role="img" aria-label="Portrait photo of Brent Holloway"></div>
  <h1 class="hero-name">Brent Holloway</h1>
  <p class="hero-role">Senior Scrum Master &amp; Team Agile Coach</p>
  <p class="hero-bio">Brent brings 13+ years of experience to his clients – experience which encompasses various project management methodologies ranging from waterfall, agile, and mixed hybrid frameworks.<br>A separating factor in the consultancy services provided at Keystride Delivery Partners, LLC is that Brent has spent years on both the Business and IT/IS sides of the project management business. Brent understands the process of driving business priorities and objectives from ideation to production while also understanding the intricacies of software development and team cadence.</p>
  <a class="btn btn-solid">Get in touch</a>
</section>

<section class="designations">
  <h2 class="section-title" style="left:468px;top:18px">Coaching Designations</h2>
  <div class="badge" style="left:140px;background:var(--orange)" role="img" aria-label="Certification badge"></div>
  <div class="badge" style="left:316px;background:var(--navy)" role="img" aria-label="Certification badge"></div>
  <div class="badge" style="left:488px;background:var(--orange)" role="img" aria-label="Certification badge"></div>
  <div class="badge" style="left:684px;background:var(--sky)" role="img" aria-label="Certification badge"></div>
  <div class="badge" style="left:888px;background:var(--navy)" role="img" aria-label="Certification badge"></div>
  <a class="btn btn-solid profile-btn" style="left:285px;width:167px">Sprint Guild Profile</a>
  <a class="btn btn-solid profile-btn" style="left:480px;width:167px">BadgeVault Profile</a>
  <a class="btn btn-solid profile-btn" style="left:672px;width:243px">LYNQ Scaled Agile Guild Profile</a>
</section>

<section class="what-we-do">
  <h2 class="section-title" style="left:523px;top:56px">What We Do</h2>
  <svg class="abs" style="left:45px;top:120px" width="545" height="545">
    <circle cx="272" cy="272" r="268" fill="none" stroke="#333" stroke-width="1.2" stroke-dasharray="8 6"/>
    <circle cx="272" cy="272" r="158" fill="none" stroke="#222" stroke-width="1.2"/>
  </svg>
  <div class="abs" style="left:182px;top:258px;width:270px;height:270px;border-radius:50%;background:#fff;box-shadow:0 16px 30px rgba(30,60,100,.18);display:flex;align-items:center;justify-content:center;gap:10px">
    <span class="brand-dot"></span><div class="brand-text">PINS &amp; DIALS<small>AGILE IT COACHING &amp; TRAINING L.L.C</small></div>
  </div>
  <div class="service" style="left:630px;top:158px">
    <svg width="42" height="42" viewBox="0 0 42 42"><circle cx="21" cy="21" r="13" fill="none" stroke="var(--brand)" stroke-width="2.4" stroke-dasharray="6 3"/><circle cx="21" cy="21" r="5" fill="var(--brand)"/></svg>Sr. Scrum Master</div>
  <div class="service" style="left:888px;top:162px">
    <svg width="50" height="50" viewBox="0 0 50 50"><rect x="13" y="13" width="24" height="24" rx="3" fill="none" stroke="var(--brand)" stroke-width="2.4"/><path d="M19 13V5M31 13V5M19 37v8M31 37v8M13 19H5M13 31H5M37 19h8M37 31h8" stroke="var(--brand)" stroke-width="2"/></svg>Advanced LYNQ<br>Scrum Master</div>
  <div class="service" style="left:630px;top:372px">
    <svg width="50" height="48" viewBox="0 0 50 48"><rect x="4" y="10" width="42" height="28" fill="none" stroke="var(--brand)" stroke-width="2.4"/><path d="M10 32l8-8 7 5 12-12" fill="none" stroke="var(--brand)" stroke-width="2.2"/><path d="M18 44h14" stroke="var(--brand)" stroke-width="2.4"/></svg>Business (Finance<br>Transformation<br>Program Manager</div>
  <div class="service" style="left:888px;top:377px">
    <svg width="50" height="50" viewBox="0 0 50 50"><rect x="6" y="4" width="32" height="38" fill="none" stroke="var(--brand)" stroke-width="2.4"/><path d="M12 14h20M12 21h14M12 28h10" stroke="var(--brand)" stroke-width="2"/><circle cx="37" cy="36" r="8" fill="#fff" stroke="var(--brand)" stroke-width="2.4"/></svg>Hybrid Scrum Master/<br>Project Manager</div>
</section>

<h2 class="section-title" style="left:478px;top:1745px">What Is My Experience</h2>
<div class="exp-band"></div>
<svg class="abs" style="left:0;top:2355px" width="85" height="50"><polygon points="0,0 85,50 0,50" fill="#3b3b3b"/></svg>

<article class="exp-card" style="left:62px;top:1820px">
  <h3>As a LYNQ Adv Scrum Master, I:</h3>
  <ul>
    <li><svg width="13" height="13"><circle cx="6.5" cy="6.5" r="5.5" fill="none" stroke="#fff"/><path d="M4 6.5l2 2 3-4" fill="none" stroke="#fff"/></svg>Stand up teams</li>
    <li class="gap"><svg width="13" height="13"><circle cx="6.5" cy="6.5" r="5.5" fill="none" stroke="#fff"/><path d="M4 6.5l2 2 3-4" fill="none" stroke="#fff"/></svg>Run development efforts concurrently leading multiple teams</li>
    <li><svg width="13" height="13"><circle cx="6.5" cy="6.5" r="5.5" fill="none" stroke="#fff"/><path d="M4 6.5l2 2 3-4" fill="none" stroke="#fff"/></svg>Run LYNQ ceremonies</li>
    <li><svg width="13" height="13"><circle cx="6.5" cy="6.5" r="5.5" fill="none" stroke="#fff"/><path d="M4 6.5l2 2 3-4" fill="none" stroke="#fff"/></svg>Scrum of Scrums facilitator</li>
    <li><svg width="13" height="13"><circle cx="6.5" cy="6.5" r="5.5" fill="none" stroke="#fff"/><path d="M4 6.5l2 2 3-4" fill="none" stroke="#fff"/></svg>PI Planning team facilitator (multiple teams on BQR)</li>
    <li class="gap"><svg width="13" height="13"><circle cx="6.5" cy="6.5" r="5.5" fill="none" stroke="#fff"/><path d="M4 6.5l2 2 3-4" fill="none" stroke="#fff"/></svg>Teach and coach to advanced development team strategies</li>
    <li><svg width="13" height="13"><circle cx="6.5" cy="6.5" r="5.5" fill="none" stroke="#fff"/><path d="M4 6.5l2 2 3-4" fill="none" stroke="#fff"/></svg>Lead program level communications and business status updates on behalf of the team</li>
  </ul>
</article>

<article class="exp-card" style="left:428px">
  <h3>As a Hybrid Scrum Master / Project Manager, I</h3>
  <ul>
    <li><svg width="13" height="13"><circle cx="6.5" cy="6.5" r="5.5" fill="none" stroke="#fff"/><path d="M4 6.5l2 2 3-4" fill="none" stroke="#fff"/></svg>Stand up teams</li>
    <li class="gap"><svg width="13" height="13"><circle cx="6.5" cy="6.5" r="5.5" fill="none" stroke="#fff"/><path d="M4 6.5l2 2 3-4" fill="none" stroke="#fff"/></svg>Run development efforts concurrently leading multiple teams</li>
    <li><svg width="13" height="13"><circle cx="6.5" cy="6.5" r="5.5" fill="none" stroke="#fff"/><path d="M4 6.5l2 2 3-4" fill="none" stroke="#fff"/></svg>Run LYNQ ceremonies</li>
    <li><svg width="13" height="13"><circle cx="6.5" cy="6.5" r="5.5" fill="none" stroke="#fff"/><path d="M4 6.5l2 2 3-4" fill="none" stroke="#fff"/></svg>Scrum of Scrums facilitator</li>
    <li><svg width="13" height="13"><circle cx="6.5" cy="6.5" r="5.5" fill="none" stroke="#fff"/><path d="M4 6.5l2 2 3-4" fill="none" stroke="#fff"/></svg>PI Planning team facilitator (multiple teams on BQR)</li>
    <li class="gap"><svg width="13" height="13"><circle cx="6.5" cy="6.5" r="5.5" fill="none" stroke="#fff"/><path d="M4 6.5l2 2 3-4" fill="none" stroke="#fff"/></svg>Teach and coach to advanced development team strategies</li>
    <li><svg width="13" height="13"><circle cx="6.5" cy="6.5" r="5.5" fill="none" stroke="#fff"/><path d="M4 6.5l2 2 3-4" fill="none" stroke="#fff"/></svg>Lead program level communications and business status updates on behalf of the team</li>
  </ul>
</article>

<article class="exp-card" style="left:798px">
  <h3>Business Transformation Program Manager</h3>
  <ul>
    <li><svg width="13" height="13"><circle cx="6.5" cy="6.5" r="5.5" fill="none" stroke="#fff"/><path d="M4 6.5l2 2 3-4" fill="none" stroke="#fff"/></svg>Stand up teams</li>
    <li class="gap"><svg width="13" height="13"><circle cx="6.5" cy="6.5" r="5.5" fill="none" stroke="#fff"/><path d="M4 6.5l2 2 3-4" fill="none" stroke="#fff"/></svg>Run development efforts concurrently leading multiple teams</li>
    <li><svg width="13" height="13"><circle cx="6.5" cy="6.5" r="5.5" fill="none" stroke="#fff"/><path d="M4 6.5l2 2 3-4" fill="none" stroke="#fff"/></svg>Run LYNQ ceremonies</li>
    <li><svg width="13" height="13"><circle cx="6.5" cy="6.5" r="5.5" fill="none" stroke="#fff"/><path d="M4 6.5l2 2 3-4" fill="none" stroke="#fff"/></svg>Scrum of Scrums facilitator</li>
    <li><svg width="13" height="13"><circle cx="6.5" cy="6.5" r="5.5" fill="none" stroke="#fff"/><path d="M4 6.5l2 2 3-4" fill="none" stroke="#fff"/></svg>PI Planning team facilitator (multiple teams on BQR)</li>
    <li class="gap"><svg width="13" height="13"><circle cx="6.5" cy="6.5" r="5.5" fill="none" stroke="#fff"/><path d="M4 6.5l2 2 3-4" fill="none" stroke="#fff"/></svg>Teach and coach to advanced development team strategies</li>
    <li><svg width="13" height="13"><circle cx="6.5" cy="6.5" r="5.5" fill="none" stroke="#fff"/><path d="M4 6.5l2 2 3-4" fill="none" stroke="#fff"/></svg>Lead program level communications and business status updates on behalf of the team</li>
  </ul>
</article>

<h2 class="cta-title">WHERE DOES COACHING COME IN TO PLAY</h2>
<a class="btn btn-light">Get in touch</a>

<footer class="site-footer">
  <div class="abs" style="left:72px;top:62px;display:flex;align-items:center;gap:12px">
    <span class="brand-dot" style="background:#fff;width:40px;height:40px"></span>
    <div class="brand-text" style="color:#fff;font-size:26px">PINS &amp; DIALS<small style="font-size:11px">AGILE IT COACHING &amp; TRAINING L.L.C</small></div>
  </div>
  <h4 class="footer-title" style="left:405px;top:44px">Contact Us</h4>
  <div class="abs" style="left:410px;top:80px;font-size:12.5px;display:flex;gap:8px;align-items:center">
    <svg width="18" height="14" viewBox="0 0 18 14"><rect x="1" y="1" width="16" height="12" fill="none" stroke="#fff" stroke-width="1.4"/><path d="M1 1l8 6 8-6" fill="none" stroke="#fff" stroke-width="1.4"/></svg>mail@company.com</div>
  <div class="abs" style="left:410px;top:115px;font-size:12.5px;display:flex;gap:8px;align-items:center">
    <svg width="16" height="16" viewBox="0 0 16 16"><path d="M3 1l3 3-2 2c1 2 3 4 5 5l2-2 3 3-2 3C7 14 2 9 1 3z" fill="none" stroke="#fff" stroke-width="1.3"/></svg>0000 000 000</div>
  <h4 class="footer-title" style="left:624px;top:44px">Quicklinks</h4>
  <ul class="footer-links">
    <li>Home</li><li>Agile Team Coaching</li><li>Coaching @ the Team Level</li><li>Coaching @ the Program Level ; LYNQ BQR Level</li><li>Why is Pins &amp; Dials Here</li><li>Portfolio</li><li>Blog</li>
  </ul>
  <div class="abs" style="left:1003px;top:44px;display:flex;gap:20px" aria-label="Social links">
    <span style="width:24px;height:24px;border-radius:50%;background:#fff"></span>
    <span style="width:24px;height:24px;border-radius:50%;background:#fff"></span>
    <span style="width:24px;height:24px;border-radius:50%;background:#fff"></span>
    <span style="width:24px;height:24px;border-radius:50%;background:#fff"></span>
  </div>
</footer>

</body>
</html>
```